Wedding Invite for Same Sex Marriage

Looking for creative ideas for our wedding invite, then other cards/information to accompany the invite i.e RSVP, Info Card, Wishing Well.We're a same sex male couple. Our thoughts are something along the lines of the Tumbleweed cartoon series. We put something together quickly for our Save The Date attached. These were printed in various bright colours. Don't stick to this design, be creative with the theme.Love to see what ideas you have.

Font styles to use
Sans Serif
Decorative
Script

Colors

Designer to choose colors to be used in the design.

Requirements
Must have
• Standard details of our names, location and time
Nice to have
• Unsure, looking for ideas from a creative crowd. Probably standard print sizes
Should not have
• Traditional, not cutesy cartoon

```html
<!DOCTYPE html>
<html lang="en">
<head>
<meta charset="utf-8">
<title>Save the Date – Archer &amp; Tumbleweed</title>
<link rel="stylesheet" href="https://fonts.googleapis.com/css2?family=Luckiest+Guy&family=Righteous&family=Caveat+Brush&family=Kalam:wght@700&display=block">
<style>
  :root {
    --magenta: #e916d3;
    --magenta-soft: #f03adf;
    --magenta-deep: #7a0a6e;
    --ink: #000000;
    --shadow: #1c1c1c;
    --paper: #ffffff;
    --rule: #bdbdbd;
    --backdrop-light: #f1f1f1;
    --backdrop-dark: #d6d6d6;
  }
  * { box-sizing: border-box; margin: 0; padding: 0; }
  html, body { width: 1200px; height: 1200px; overflow: hidden; }
  body {
    position: relative;
    background: radial-gradient(circle at 50% 45%, var(--backdrop-light) 0%, var(--backdrop-dark) 100%);
  }

  /* Save the date card */
  .save-card {
    position: absolute;
    left: 176px; top: 42px;
    width: 849px; height: 598px;
    background: var(--ink);
  }
  .save-card__text {
    position: absolute;
    left: 0; top: 0;
    width: 412px; height: 100%;
    text-align: center;
  }
  .headline {
    position: absolute;
    left: 0; width: 100%;
    top: 38px;
    font-family: "Luckiest Guy", "Righteous", sans-serif;
    font-weight: 400;
    font-size: 54px;
    line-height: 68px;
    color: var(--paper);
    text-transform: uppercase;
  }
  .event-date {
    position: absolute;
    left: 0; width: 100%;
    top: 252px;
    font-family: "Caveat Brush", "Kalam", cursive;
    font-size: 36px;
    line-height: 44px;
    color: var(--magenta);
    transform: skewX(-8deg);
  }
  .couple {
    position: absolute;
    left: 0; width: 100%;
    top: 326px;
    font-family: "Righteous", sans-serif;
    font-size: 36px;
    line-height: 52px;
    color: var(--paper);
  }
  .announcement {
    position: absolute;
    left: 0; width: 100%;
    top: 478px;
    font-family: "Caveat Brush", "Kalam", cursive;
    font-size: 52px;
    line-height: 52px;
    color: var(--magenta);
    text-transform: uppercase;
    transform: skewX(-10deg);
  }
  .announcement__heart {
    position: absolute;
    left: 92px; top: -12px;
    width: 24px; height: 22px;
  }
  .save-card__artwork {
    position: absolute;
    left: 402px; top: 24px;
    width: 407px; height: 550px;
  }
  .artwork-fill {
    position: absolute;
    inset: 0;
    background:
      radial-gradient(ellipse 38% 62% at 52% 62%, var(--shadow) 0%, var(--shadow) 55%, rgba(28,28,28,0) 100%),
      linear-gradient(160deg, var(--magenta-soft), var(--magenta) 60%, var(--magenta-deep));
  }
  .artwork-lines {
    position: absolute;
    inset: 0;
  }

  /* RSVP card */
  .rsvp-card {
    position: absolute;
    left: 414px; top: 652px;
    width: 372px; height: 524px;
    background: var(--ink);
    text-align: center;
  }
  .rsvp-card__artwork {
    position: absolute;
    left: 10px; top: 42px;
    width: 350px; height: 118px;
    background:
      radial-gradient(ellipse 10% 45% at 20% 60%, var(--ink) 0%, rgba(0,0,0,0) 100%),
      radial-gradient(ellipse 10% 45% at 48% 60%, var(--ink) 0%, rgba(0,0,0,0) 100%),
      linear-gradient(160deg, var(--magenta-soft), var(--magenta));
  }
  .rsvp-divider {
    position: absolute;
    left: 214px; top: 42px;
    width: 2px; height: 118px;
    background: var(--ink);
  }
  .rsvp-title {
    position: absolute;
    left: 0; width: 100%;
    top: 206px;
    font-family: "Righteous", sans-serif;
    font-weight: 400;
    font-size: 52px;
    color: var(--paper);
    letter-spacing: 2px;
  }
  .rsvp-prompt {
    position: absolute;
    left: 0; width: 100%;
    top: 295px;
    font-family: "Kalam", cursive;
    font-weight: 700;
    font-size: 14px;
    color: var(--magenta);
  }
  .rsvp-line {
    position: absolute;
    left: 50px; top: 374px;
    width: 272px;
    border-top: 1px dashed var(--rule);
  }
  .rsvp-contact {
    position: absolute;
    left: 98px; top: 441px;
    font-family: "Kalam", cursive;
    font-weight: 700;
    font-size: 13px;
    color: var(--magenta);
  }
</style>
</head>
<body>

<section class="save-card">
  <div class="save-card__text">
    <h1 class="headline">Save the<br>Date</h1>
    <p class="event-date">21.03.20</p>
    <p class="couple">Archer &amp;<br>Tumbleweed</p>
    <p class="announcement">
      <svg class="announcement__heart" viewBox="0 0 22 20" aria-hidden="true">
        <path d="M11 19 L2 10 A5 5 0 0 1 11 4 A5 5 0 0 1 20 10 Z" fill="var(--magenta)"/>
      </svg>
      Are getting<br>married
    </p>
  </div>

  <div class="save-card__artwork">
    <div class="artwork-fill" role="img" aria-label="Illustration of two grooms in tuxedos and bow ties standing side by side in silhouette, with a heart on a stick, against a patterned magenta backdrop"></div>
    <svg class="artwork-lines" viewBox="0 0 407 550" aria-hidden="true">
      <rect x="59" y="0" width="6" height="550" fill="var(--ink)"/>
      <rect x="0" y="498" width="407" height="29" fill="var(--ink)"/>
      <circle cx="407" cy="0" r="48" fill="var(--ink)"/>
    </svg>
  </div>
</section>

<section class="rsvp-card">
  <div class="rsvp-card__artwork" role="img" aria-label="Illustration of two men standing in silhouette beside a profile silhouette, on a magenta band"></div>
  <div class="rsvp-divider"></div>
  <h2 class="rsvp-title">RSVP</h2>
  <p class="rsvp-prompt">Kindly Reply</p>
  <div class="rsvp-line"></div>
  <p class="rsvp-contact">contact :</p>
</section>

</body>
</html>
```